Semi Permanent make up flyer

Hi

I will be sending a few thousand flyers dropped door to door in some very lovely parts of London.

The flyer must contain the following information;

New studio in Greenwich

Velline Arc trained technician - gold advanced level

Free consultation no obligation

Price List;
Eyebrow hair stroke: £325
Eyebrows 3D effect: £395
Microblading hair stroke: £330
Eyelash enhancement Top: £250
Eyelash enhancement Top & Bottom: £300
Lip blush: £450

Tel;……………….
Facebook: Odrelle Permanent Cosmetics
Instagram: Odrelle_Permanent_Cosmetics

Special introductory offers - available for a limited time only;
Like & share my page for 10% off any treatment
Refer a friend for £50 off each
Buy one treatment get 50% off another

I would like it to look clean, professional, expensive, and high end/luxury

I’m happy to make this a double sided print so I can have my logo on the front and the information on the back.

It must include my logo.

If you could use images of appealing women I think it would work best. Images have to have nice eyes, lips and brows. Weather you use entire face or features that is up to you.

Please show me a selection of different colour ways across the whole design. I personally feel softer tones would work. No black or bright colours.

I will be getting my new phone number in the next few days. I will let you know via messages what it is for you to add it in.

Any questions feel free to ask.

Target Market(s)

Women

Industry/Entity Type

Beauty Salon

Font styles to use
Sans Serif

Requirements
Must have
• Everything in Description
Nice to have
• The designers give their ideas. Im looking for input
Should not have
• Childish, cheap images or fonts. This is very high end so needs to look it

```html
<!DOCTYPE html>
<html lang="en">
<head>
<meta charset="utf-8">
<title>Odrelle Permanent Cosmetics – Flyer</title>
<link href="https://fonts.googleapis.com/css2?family=Montserrat:wght@400;600;700&family=Mulish:wght@400;600&display=swap" rel="stylesheet">
<style>
  :root {
    --stage: #a09fa0;
    --gold: #c08a2a;
    --gold-dark: #a8751f;
    --gold-light: #f3c466;
    --slate: #6a6a6a;
    --ink: #2b2b2b;
    --white: #ffffff;
    --orange: #f29a1f;
  }
  * { margin: 0; padding: 0; box-sizing: border-box; }
  html, body { width: 1200px; height: 900px; overflow: hidden; }
  body {
    background: var(--stage);
    position: relative;
    font-family: "Mulish", sans-serif;
  }

  /* Front side */
  .flyer-front {
    position: absolute; left: 57px; top: 227px; width: 572px; height: 404px;
    box-shadow: 3px 4px 6px rgba(0,0,0,.45);
    overflow: hidden;
  }
  .front-photo {
    position: absolute; inset: 0;
    background:
      radial-gradient(ellipse 160px 200px at 450px 260px, #c98e72 0%, rgba(150,80,50,.85) 45%, rgba(110,60,40,0) 80%),
      radial-gradient(ellipse 280px 260px at 130px 120px, #f4efee 0%, #d9cccc 60%, #bba9a8 100%);
  }
  .front-brand {
    position: absolute; left: 70px; top: 50px; width: 140px;
    text-align: center; color: var(--gold);
    font-family: "Montserrat", sans-serif; font-weight: 400;
  }
  .front-brand .mark {
    display: block; width: 62px; height: 62px; margin: 0 auto 22px;
    border-radius: 50%; background: var(--gold);
  }
  .front-brand .name { display: block; font-size: 17px; letter-spacing: 5px; line-height: 20px; }
  .front-brand .sub { display: block; font-size: 8px; letter-spacing: 1.5px; line-height: 12px; margin-top: 2px; }

  /* Back side */
  .flyer-back {
    position: absolute; left: 666px; top: 95px; width: 471px; height: 668px;
    background: var(--white);
    box-shadow: 3px 4px 6px rgba(0,0,0,.45);
    overflow: hidden;
  }
  .headline {
    position: absolute; left: 18px; top: 33px;
    color: var(--gold); font-family: "Montserrat", sans-serif; line-height: 1;
  }
  .headline .big { font-size: 48px; font-weight: 400; display: block; }
  .headline .mid { font-size: 23px; font-weight: 400; display: block; margin-top: 4px; }
  .headline .place { font-size: 29px; font-weight: 700; display: block; margin-top: 8px; }

  .back-brand {
    position: absolute; left: 176px; top: 18px; width: 110px;
    text-align: center; color: var(--gold);
    font-family: "Montserrat", sans-serif; font-weight: 400;
  }
  .back-brand .mark {
    display: block; width: 52px; height: 52px; margin: 0 auto 18px;
    border-radius: 50%; background: var(--gold);
  }
  .back-brand .name { display: block; font-size: 13px; letter-spacing: 3.5px; line-height: 15px; }
  .back-brand .sub { display: block; font-size: 6.5px; letter-spacing: .8px; line-height: 9px; }

  .contact {
    position: absolute; right: 14px; top: 11px; text-align: right;
    font-size: 9.5px; color: var(--ink);
  }
  .contact li { list-style: none; display: flex; justify-content: flex-end; align-items: center; gap: 5px; height: 19px; }
  .contact .phone { font-size: 12px; }
  .contact .icon { width: 14px; height: 14px; }
  .credential {
    position: absolute; right: 13px; top: 73px; text-align: right;
    color: var(--gold); font-size: 12.5px; line-height: 15px;
  }
  .consult {
    position: absolute; right: 13px; top: 120px; text-align: right;
    color: var(--ink); font-size: 19px; line-height: 24px;
  }
  .consult .free { color: var(--gold); font-size: 26px; }

  .info-panel {
    position: absolute; left: 0; top: 173px; width: 471px; height: 324px;
    background: var(--slate); color: var(--white);
  }
  .pill {
    background: linear-gradient(90deg, var(--gold-dark), var(--gold-light) 50%, var(--gold-dark));
    color: var(--ink); text-align: center;
    box-shadow: 0 2px 3px rgba(0,0,0,.3);
  }
  .price-title {
    position: absolute; left: 170px; top: 13px; width: 131px; height: 22px;
    border-radius: 4px; font-size: 15px; line-height: 22px; font-weight: 600;
  }
  .price-list { position: absolute; left: 48px; top: 42px; width: 366px; }
  .price-list li {
    list-style: none; display: flex; justify-content: space-between;
    font-size: 12.5px; height: 20.2px; line-height: 20px;
  }
  .offers-title {
    position: absolute; left: 55px; top: 176px; width: 360px; height: 52px;
    border-radius: 10px; padding-top: 4px;
  }
  .offers-title strong { display: block; font-family: "Montserrat", sans-serif; font-size: 22px; font-weight: 700; line-height: 26px; }
  .offers-title span { display: block; font-size: 14px; line-height: 16px; }
  .offers { position: absolute; left: 0; top: 240px; width: 471px; text-align: center; }
  .offers li { list-style: none; font-size: 12.5px; height: 21px; line-height: 21px; }
  .offers b { font-family: "Montserrat", sans-serif; font-size: 19px; font-weight: 700; }

  .feature-lips, .feature-eye { position: absolute; top: 497px; height: 151px; }
  .feature-lips {
    left: 0; width: 235px;
    background: radial-gradient(ellipse 130px 60px at 120px 70px, #f08a6c 0%, #e57a5e 45%, #c99c8a 75%, #dcc0b4 100%);
  }
  .feature-eye {
    left: 236px; width: 235px;
    background: radial-gradient(ellipse 90px 45px at 95px 65px, #3e5a3c 0%, #5d6e7a 40%, #b0b4c8 75%, #c9c6d4 100%);
  }
  .base-band {
    position: absolute; left: 0; bottom: 0; width: 471px; height: 20px;
    background: linear-gradient(90deg, var(--gold-dark), var(--gold-light) 55%, var(--gold-dark));
  }
</style>
</head>
<body>

<section class="flyer-front">
  <div class="front-photo" role="img" aria-label="Portrait photo of a woman with brown hair and soft make-up, arms raised above her head, on a pale backdrop"></div>
  <div class="front-brand">
    <span class="mark"></span>
    <span class="name">ODRELLE</span>
    <span class="sub">PERMANENT COSMETICS</span>
  </div>
</section>

<section class="flyer-back">
  <h1 class="headline">
    <span class="big">New</span>
    <span class="mid">studio in</span>
    <span class="place">Greenwich</span>
  </h1>

  <div class="back-brand">
    <span class="mark"></span>
    <span class="name">ODRELLE</span>
    <span class="sub">PERMANENT COSMETICS</span>
  </div>

  <ul class="contact">
    <li class="phone">0198-204-617
      <svg class="icon" viewBox="0 0 14 14"><circle cx="7" cy="7" r="7" fill="var(--orange)"/><path d="M4.3 3.6l1.4-.3.8 1.8-.9.7a5 5 0 0 0 2.6 2.6l.7-.9 1.8.8-.3 1.4c-3.4.2-6.3-2.7-6.1-6.1z" fill="#fff"/></svg>
    </li>
    <li>Odrelle Permanent Cosmetics
      <svg class="icon" viewBox="0 0 14 14"><circle cx="7" cy="7" r="7" fill="var(--orange)"/></svg>
    </li>
    <li>Odrelle_Permanent_Cosmetics
      <svg class="icon" viewBox="0 0 14 14"><circle cx="7" cy="7" r="7" fill="var(--orange)"/></svg>
    </li>
  </ul>

  <p class="credential">Velline Arc trained<br>technician -<br>gold advanced level</p>
  <p class="consult"><span class="free">Free</span> consultation<br>No obligation</p>

  <div class="info-panel">
    <h2 class="pill price-title">Price List</h2>
    <ul class="price-list">
      <li><span>Eyebrow hair stroke:</span><span>£325</span></li>
      <li><span>Eyebrows 3D effect:</span><span>£395</span></li>
      <li><span>Microblading hair stroke:</span><span>£330</span></li>
      <li><span>Eyelash enhancement Top:</span><span>£250</span></li>
      <li><span>Eyelash enhancement Top &amp; Bottom:</span><span>£300</span></li>
      <li><span>Lip blush:</span><span>£450</span></li>
    </ul>

    <div class="pill offers-title">
      <strong>Special introductory offers -</strong>
      <span>available for a limited time only;</span>
    </div>
    <ul class="offers">
      <li>Like &amp; share my page for <b>10%</b> off any treatment</li>
      <li>Refer a friend for <b>£50</b> off each</li>
      <li>Buy one treatment get <b>50%</b> off another</li>
    </ul>
  </div>

  <div class="feature-lips" role="img" aria-label="Close-up photo of lips with coral lip blush"></div>
  <div class="feature-eye" role="img" aria-label="Close-up photo of a green eye with eyeliner and lash enhancement"></div>
  <div class="base-band"></div>
</section>

</body>
</html>
```